Verdant Loop Advisors, LLC

I am looking for a simple, clear layout with my logo prominent and embossed, on the best quality card stock available. I would like the business name and phone number included on the card as well......I dont want my name anywhere on the card and I would like my logo embossed on the card......something simple with a white back......open to designs as long as they go along with recycling symbols and green type stuff.....The address, website, cell number, fax number, and email are listed below

5374 Tillbury Fenwood Road
Larkmont, MD 20799

c. 240.555.0143 f. 240.555.0187
e. sales@verdantloopadvisors.example
w. www.verdantloopadvisors.example

Industry/Entity Type

Recycling

```html
<!DOCTYPE html>
<html lang="en">
<head>
<meta charset="utf-8">
<title>Verdant Loop Advisors, LLC — Business Card</title>
<link rel="stylesheet" href="https://fonts.googleapis.com/css2?family=Arimo:wght@400;700&display=swap">
<style>
  :root {
    --backdrop: #e2e3e2;
    --card: #fbfbfb;
    --ink: #2a2623;
    --green: #2f6b3a;
    --green-bright: #2e9a45;
    --rule: #2f8a43;
  }
  * { box-sizing: border-box; margin: 0; padding: 0; }
  html, body {
    width: 1200px; height: 675px; overflow: hidden;
    background: var(--backdrop);
    font-family: "Arimo", Arial, sans-serif;
    color: var(--ink);
  }
  .sheet {
    position: relative; width: 1200px; height: 675px;
    display: flex; align-items: center; justify-content: center; gap: 40px;
  }
  .card {
    position: relative; width: 540px; height: 309px;
    background: var(--card);
    box-shadow: 0 2px 10px rgba(0,0,0,0.12);
    overflow: hidden;
  }
  .card__band {
    position: absolute; left: 0; right: 0; bottom: 0; height: 9px;
    background: var(--green);
  }
  .wordmark {
    display: flex; align-items: center; gap: 12px;
  }
  .wordmark__square {
    width: 30px; height: 30px; background: var(--green); flex: none;
  }
  .wordmark__name {
    font-weight: 700; color: var(--ink); letter-spacing: 0.02em;
    line-height: 1.15;
  }
  .card--front .wordmark {
    position: absolute; left: 70px; top: 126px;
  }
  .card--front .wordmark__name { font-size: 27px; }
  .card--back .wordmark {
    position: absolute; left: 30px; top: 130px;
  }
  .card--back .wordmark__square { width: 22px; height: 22px; }
  .card--back .wordmark__name { font-size: 17px; width: 180px; }
  .contact {
    position: absolute; left: 262px; top: 96px; width: 262px;
    font-size: 12.5px; line-height: 1.5;
  }
  .contact__address { margin-bottom: 8px; }
  .contact__rule {
    height: 1.5px; background: var(--rule); margin: 5px 0 6px;
  }
  .contact__label { color: var(--green-bright); font-weight: 700; margin-right: 4px; }
  .contact__domain { color: var(--green-bright); }
</style>
</head>
<body>
<main class="sheet">
  <section class="card card--front" aria-label="Card front">
    <div class="wordmark">
      <span class="wordmark__square"></span>
      <span class="wordmark__name">Verdant Loop Advisors, LLC</span>
    </div>
    <div class="card__band"></div>
  </section>

  <section class="card card--back" aria-label="Card back">
    <div class="wordmark">
      <span class="wordmark__square"></span>
      <span class="wordmark__name">Verdant Loop Advisors, LLC</span>
    </div>
    <div class="contact">
      <p class="contact__address">5374 Tillbury Fenwood Road<br>Larkmont, MD 20799</p>
      <p><span class="contact__label">c.</span>240.555.0143</p>
      <p><span class="contact__label">f.</span>240.555.0187</p>
      <p><span class="contact__label">e.</span>sales@verdantloopadvisors.example</p>
      <div class="contact__rule"></div>
      <p><span class="contact__label">w.</span>www.<span class="contact__domain">verdantloopadvisors</span>.example</p>
    </div>
    <div class="card__band"></div>
  </section>
</main>
</body>
</html>
```